OPV Brantmoor Freight Limited

We need the buissnes card to be very exclusive. As we are all young in our company. We need this to be the gate to make our clients feel deep interest for us.

We are focused in as International Trade advisors, and our products go from Oil Tanker Ships to Rubber balls for dogs.

Our Slogan is Closer Across Oceans.
And our main marketing will be through Internet.

We were stablished in 2009 In Mexico and we also have offices in Hong Kong.
We have representatives in China and Europe.

Target Market(s)

Is every company or Individual that wants to develop an International Project or product development or Logistic service of Goods and people.
Some of our current projects are Ship Brokerage, Mine Brokerage, Real State and Product Pormotional development.

Industry/Entity Type

It Company

Requirements
Must have
• Our Logo and slogan, and make the card accoriding to the logo.
Nice to have
• Our Colors

```html
<!DOCTYPE html>
<html lang="en">
<head>
<meta charset="utf-8">
<title>OPV Brantmoor Freight Limited — Business Card</title>
<link href="https://fonts.googleapis.com/css2?family=Roboto:wght@300;400;500;700&family=Noto+Sans+SC:wght@500;700&display=swap" rel="stylesheet">
<style>
  :root {
    --stage: #3a332e;
    --card-black: #141414;
    --card-white: #ffffff;
    --brand-green: #7ac143;
    --brand-blue: #29abe2;
    --ink: #2b2b2b;
    --ink-soft: #4a4a4a;
  }
  * { box-sizing: border-box; margin: 0; padding: 0; }
  html, body {
    width: 1200px; height: 716px; overflow: hidden;
    background: var(--stage);
    font-family: "Roboto", Arial, sans-serif;
  }
  .stage {
    position: relative; width: 1200px; height: 716px;
    display: flex; align-items: center; justify-content: center; gap: 40px;
  }
  .card {
    position: relative; width: 520px; height: 297px; overflow: hidden;
    box-shadow: 0 10px 30px rgba(0,0,0,.45);
  }

  /* Back of card */
  .card--back { background: var(--card-black); }
  .card--back .brand { position: absolute; right: 48px; top: 92px; }
  .brand-mark {
    display: flex; align-items: center; gap: 12px;
    color: var(--brand-green); font-weight: 700; letter-spacing: 4px;
  }
  .brand-mark .dot { border-radius: 50%; background: var(--brand-green); flex: none; }
  .card--back .brand-mark { font-size: 64px; line-height: 1; }
  .card--back .brand-mark .dot { width: 26px; height: 26px; }
  .tagline { color: var(--brand-blue); font-weight: 400; white-space: nowrap; }
  .card--back .tagline { font-size: 13px; margin-top: 4px; }
  .card--back .website {
    position: absolute; right: 48px; bottom: 40px;
    color: var(--brand-blue); font-size: 14px;
  }

  /* Front of card */
  .card--front { background: var(--card-white); }
  .band-top { position: absolute; left: 0; right: 0; top: 0; height: 10px; background: var(--brand-green); }
  .band-bottom { position: absolute; left: 0; right: 0; bottom: 0; height: 14px; background: var(--brand-blue); }
  .company { position: absolute; left: 26px; top: 62px; width: 200px; }
  .card--front .brand-mark { font-size: 50px; line-height: 1; }
  .card--front .brand-mark .dot { width: 20px; height: 20px; }
  .card--front .tagline { font-size: 10.5px; margin-top: 3px; }
  .company-name { margin-top: 22px; font-size: 12.5px; color: var(--ink-soft); line-height: 1.3; }
  .company-name .zh { font-family: "Noto Sans SC", sans-serif; font-weight: 500; font-size: 13px; color: var(--ink); }
  .divider { position: absolute; left: 236px; top: 52px; width: 1.5px; height: 190px; background: var(--brand-green); }
  .contact {
    position: absolute; left: 256px; top: 42px; right: 16px;
    color: var(--ink-soft); font-size: 12px; line-height: 1.35;
  }
  .person-name { font-size: 16px; color: var(--ink); font-weight: 400; white-space: nowrap; }
  .person-name .zh { font-family: "Noto Sans SC", sans-serif; font-weight: 700; }
  .person-title { font-size: 11.5px; margin-bottom: 6px; }
  .lines { display: grid; grid-template-columns: 16px 1fr; column-gap: 6px; }
  .address { margin-top: 10px; }
  .address .zh { font-family: "Noto Sans SC", sans-serif; font-weight: 700; color: var(--ink); font-size: 12.5px; }
</style>
</head>
<body>
<main class="stage">
  <section class="card card--back" aria-label="Business card back">
    <div class="brand">
      <div class="brand-mark"><span class="dot"></span>OPV</div>
      <div class="tagline">Closer Across Oceans</div>
    </div>
    <div class="website">www.brantmoorfreight.com</div>
  </section>

  <section class="card card--front" aria-label="Business card front">
    <div class="band-top"></div>
    <div class="company">
      <div class="brand-mark"><span class="dot"></span>OPV</div>
      <div class="tagline">Closer Across Oceans</div>
      <div class="company-name">
        Brantmoor Freight Limited<br>
        <span class="zh">布兰特摩尔货运有限公司</span>
      </div>
    </div>
    <div class="divider"></div>
    <div class="contact">
      <div class="person-name">Mateo Villanueva R. <span class="zh">马特奥</span></div>
      <div class="person-title">Director</div>
      <div class="lines">
        <span>T</span><span>+52 4425550137</span>
        <span>M</span><span>+5214425550182</span>
        <span>E</span><span>mvr@brantmoor.la</span>
      </div>
      <div class="address">
        Cerro del Álamo #214, col. Los Olivos<br>
        cp76150, Queretaro, Queretaro Mexico
      </div>
      <div class="address">
        Harbour Lane No.18 Room 903-5<br>
        Tsim Sha Tsui Kowloon,Hongkong<br>
        <span class="zh">香港九龙尖沙咀海港里<br>18号布兰大厦903-5室</span>
      </div>
    </div>
    <div class="band-bottom"></div>
  </section>
</main>
</body>
</html>
```